Shop front signage design for Bubble Tea Shop

Plum Harbor is Sydney based Green Tea Shop.We are looking for a modern and sleek signage for shop front end. We have Aluminium Composite Panel and Awning sign at the shop front. We will keep Aluminium composite panel simple with logo and text. We are after awning design which is above glass door and under the panel. Old Awning is PVC foam in two pieces 2310mm w x 1000mm h. We need someone to design awing. It should reflect Bubble tea and using bubble tea cups with pearls is essential. Stock images can be used. Avoid using icons or illustrative icons as we are after real images of bubble tea cup. This is to ensure that the brand is not taken as juice shop or cafe.
Panel Dimensions is 5250 mm w x 580 mm h.Awning/ Fascia sign is 4720 mm w x 1000 mm h.
Logo and signage concept is attached.

Target Market(s)

Corporate Male and Female, school, general public.

Colors
f36e22
333333
000000
eaeaea
cbcbcb

Requirements
Must have
• Bubble tea cups with fruit or milk tea.
Should not have
• Icons, illustration

```html
<!DOCTYPE html>
<html lang="en">
<head>
<meta charset="utf-8">
<title>Plum Harbor – Shop Front Awning</title>
<link href="https://fonts.googleapis.com/css2?family=Nunito:wght@800&display=swap" rel="stylesheet">
<style>
  :root {
    --page-bg: #eaeaea;
    --sign-white: #ffffff;
    --sign-black: #050505;
    --text-white: #ffffff;
    --lid-white: #f4f7fa;
    --cup-purple: #9d84c2;
    --cup-pink: #f0a2b4;
    --cup-yellow: #d8cf52;
  }
  html, body {
    margin: 0;
    padding: 0;
    width: 1200px;
    height: 1000px;
    overflow: hidden;
    background: var(--page-bg);
  }
  .awning {
    position: absolute;
    left: 52px;
    top: 418px;
    width: 1080px;
    height: 229px;
    background: var(--sign-white);
    overflow: hidden;
  }
  .awning-shapes {
    position: absolute;
    inset: 0;
  }
  .cup-photo {
    position: absolute;
    top: 14px;
    width: 172px;
    height: 198px;
    border-radius: 40px 40px 30px 30px;
    background:
      linear-gradient(180deg, var(--sign-white) 0%, rgba(255,255,255,0.85) 22%, rgba(255,255,255,0) 48%),
      linear-gradient(90deg, var(--cup-purple) 0%, var(--cup-purple) 22%, var(--cup-pink) 40%, var(--cup-pink) 66%, var(--cup-yellow) 84%, var(--cup-yellow) 100%);
  }
  .cup-photo--left { left: 45px; }
  .cup-photo--right { left: 853px; }
  .brand {
    position: absolute;
    left: 321px;
    top: 92px;
    display: flex;
    align-items: center;
    gap: 20px;
  }
  .brand-dot {
    width: 92px;
    height: 92px;
    border: 6px solid var(--text-white);
    border-radius: 50%;
    box-sizing: border-box;
    flex: none;
  }
  .brand-name {
    font-family: "Nunito", sans-serif;
    font-weight: 800;
    font-size: 54px;
    line-height: 1;
    color: var(--text-white);
    letter-spacing: -1px;
    white-space: nowrap;
  }
</style>
</head>
<body>
  <section class="awning">
    <div class="cup-photo cup-photo--left" role="img" aria-label="Photo of three bubble tea cups with tapioca pearls and blue straws: taro, strawberry and mango"></div>
    <div class="cup-photo cup-photo--right" role="img" aria-label="Photo of three bubble tea cups with tapioca pearls and blue straws: taro, strawberry and mango"></div>
    <svg class="awning-shapes" width="1080" height="229" viewBox="0 0 1080 229" aria-hidden="true">
      <polygon points="238,0 842,0 760,229 320,229" fill="var(--sign-black)"/>
      <g stroke="var(--sign-black)" stroke-width="3">
        <line x1="212" y1="0" x2="294" y2="229"/>
        <line x1="220" y1="0" x2="302" y2="229"/>
        <line x1="228" y1="0" x2="310" y2="229"/>
        <line x1="852" y1="0" x2="770" y2="229"/>
        <line x1="860" y1="0" x2="778" y2="229"/>
        <line x1="868" y1="0" x2="786" y2="229"/>
      </g>
    </svg>
    <div class="brand">
      <div class="brand-dot"></div>
      <span class="brand-name">Plum Harbor</span>
    </div>
  </section>
</body>
</html>
```